New Website for novelty yarn producer

We need a new website for our company, Merovac. We make highly tailored yarns for weavers worldwide. This year marks our 40th anniversary and we want to evolve our image and identity.

Our temporary website can be found at:
www.merovacyarns-example.com

Our only concern in that throughout the website the protagonist must be our client, we make their creations possible and are highly adaptable both during the ideation process of the yarn as well as in the production. This is at the core of the way we do business and is summarised within the concept of OBM (Open Bridge Method).

Industry/Entity Type

Textile

Number of Pages Required

1 page

Colors
9bcb3c

Requirements
Must have
• Open Bridge Method (OBM) - can be found on or current website www.merovacyarns-example.com

```html
<!DOCTYPE html>
<html lang="en">
<head>
<meta charset="utf-8">
<title>Merovac Novelty Yarn Solutions</title>
<link rel="stylesheet" href="https://fonts.googleapis.com/css2?family=Roboto:wght@300;400;500;700&display=swap">
<style>
  :root {
    --green: #9bcb3c;
    --green-deep: #6f9a2c;
    --ink: #222;
    --muted: #777;
    --white: #fff;
  }
  * { margin: 0; padding: 0; box-sizing: border-box; }
  html, body { width: 1200px; height: 1200px; overflow: hidden; background: var(--white); }
  body { font-family: "Roboto", sans-serif; color: var(--ink); }
  .stage { position: absolute; left: 0; top: 0; width: 1500px; height: 1500px; transform: scale(0.8); transform-origin: 0 0; }
  .abs { position: absolute; }
  .center { text-align: center; }

  .brand { left: 505px; top: 14px; display: flex; align-items: center; gap: 6px; }
  .brand-dot { width: 10px; height: 10px; border-radius: 50%; background: var(--green); }
  .brand-name { font-weight: 500; font-size: 18px; color: var(--ink); line-height: 20px; }

  .nav { left: 663px; top: 19px; display: flex; font-size: 6.5px; font-weight: 700; }
  .nav a { color: var(--ink); text-decoration: none; padding: 3px 0; margin-right: 14px; line-height: 6px; }
  .nav a.active { background: var(--green); color: var(--white); padding: 3px 11px; margin-right: 13px; }

  .hero { left: 441px; top: 50px; width: 616px; height: 246px; background: linear-gradient(120deg, #cde4d8 0%, #5fc2b4 15%, #1d87a8 28%, #b9cc33 42%, #d6d43a 50%, #c2264f 62%, #e23a3a 74%, #f08a24 84%, #f4c21a 92%, #f5f0e6 100%); }
  .hero-title { left: 441px; top: 105px; width: 616px; font-weight: 700; font-size: 80px; letter-spacing: 2px; color: rgba(255,255,255,0.55); text-align: center; line-height: 90px; }
  .hero-title .at { font-weight: 300; font-size: 56px; color: var(--white); margin: 0 10px; }
  .hero-sub { left: 441px; top: 219px; width: 616px; font-size: 9.5px; font-weight: 500; color: var(--white); line-height: 12.5px; text-shadow: 0 1px 2px rgba(0,0,0,.5); }
  .dots { left: 725px; top: 268px; display: flex; gap: 5px; }
  .dots span { width: 8px; height: 8px; border-radius: 50%; border: 1px solid var(--white); }
  .dots span.on { background: var(--white); }

  .feature { width: 145px; }
  .feature h3, .offer h3 { font-weight: 400; font-size: 10px; color: var(--green); margin-bottom: 7px; }
  .feature p, .offer p { font-size: 5px; line-height: 10px; color: var(--muted); }

  .band { left: 441px; width: 616px; }
  .band-obm { top: 438px; height: 267px; background: linear-gradient(180deg, #1f261c 0%, #3b4b27 45%, #6a9a34 85%, #82b43b 100%); }
  .obm-title { left: 632px; top: 505px; font-size: 21px; font-weight: 300; color: var(--white); }
  .obm-title b { color: var(--green); font-weight: 700; }
  .obm-text { left: 555px; top: 557px; width: 388px; font-size: 6.2px; line-height: 12.5px; color: rgba(255,255,255,.8); }
  .btn { width: 123px; height: 23px; font-size: 6.5px; font-weight: 500; display: flex; align-items: center; justify-content: center; gap: 12px; letter-spacing: .3px; }
  .btn-light { left: 687px; top: 634px; border: 1px solid rgba(255,255,255,.8); color: var(--white); }
  .btn-green { left: 687px; top: 1385px; border: 1px solid var(--green); color: var(--ink); }

  .section-title { font-weight: 300; font-size: 20px; }
  .section-sub { font-size: 6px; color: var(--muted); }

  .offer { width: 160px; }
  .offer-img { width: 160px; height: 112px; }
  .offer h3 { text-align: center; margin-top: 8px; margin-bottom: 6px; }

  .band-team { top: 1029px; height: 267px; background: linear-gradient(180deg, #2a2f26 0%, #3f4e2c 45%, #6a9a34 85%, #7fb13a 100%); }
  .portrait { width: 114px; height: 114px; border-radius: 50%; border: 3px solid var(--white); }
  .member { font-size: 9.5px; font-weight: 300; color: var(--white); width: 180px; }
  .member b { font-weight: 700; }

  .footer { left: 441px; top: 1462px; width: 616px; height: 38px; background: var(--green); }
  .copy { left: 505px; top: 1476px; font-size: 6.5px; color: var(--white); }
  .social { left: 929px; top: 1474px; display: flex; gap: 5px; }
  .social span { width: 12px; height: 12px; border-radius: 50%; background: var(--white); }
</style>
</head>
<body>
<div class="stage">

  <header>
    <div class="abs brand">
      <span class="brand-dot"></span>
      <span class="brand-name">Merovac</span>
    </div>
    <nav class="abs nav">
      <a class="active" href="#">Home</a>
      <a href="#">About Us</a>
      <a href="#">Open Bridge Method</a>
      <a href="#">Heritage</a>
      <a href="#">Team</a>
      <a href="#">Blog</a>
      <a href="#">Contact</a>
    </nav>
  </header>

  <section class="hero-block">
    <div class="abs hero" role="img" aria-label="Close-up of rows of multicoloured woven yarn samples in a rainbow of shades"></div>
    <div class="abs hero-title">MVYS<span class="at">at</span>40</div>
    <p class="abs hero-sub center">MVYS combines the experience of a team that has served the weaving industry<br>for over 40 years, fully dedicated to the success of our clients</p>
    <svg class="abs" style="left:455px;top:160px" width="16" height="28" viewBox="0 0 16 28"><path d="M14 1 2 14l12 13" fill="none" stroke="#fff" stroke-width="1.5"/></svg>
    <svg class="abs" style="left:1027px;top:160px" width="16" height="28" viewBox="0 0 16 28"><path d="M2 1l12 13L2 27" fill="none" stroke="#fff" stroke-width="1.5"/></svg>
    <div class="abs dots"><span></span><span class="on"></span><span class="on"></span><span class="on"></span></div>
  </section>

  <section class="values">
    <svg class="abs" style="left:572px;top:325px" width="26" height="28" viewBox="0 0 26 28" fill="#9bcb3c"><circle cx="13" cy="13" r="6"/><rect x="10" y="19" width="6" height="5" rx="1"/><path d="M13 1v4M2 13h4M20 13h4M5 5l3 3M21 5l-3 3" stroke="#9bcb3c" stroke-width="1.6"/></svg>
    <svg class="abs" style="left:736px;top:332px" width="26" height="24" viewBox="0 0 26 24"><ellipse cx="12" cy="12" rx="11" ry="10" fill="#9bcb3c"/><circle cx="7" cy="9" r="2" fill="#fff"/><circle cx="12" cy="6" r="2" fill="#fff"/><circle cx="8" cy="15" r="2" fill="#fff"/><path d="M16 18 25 3" stroke="#9bcb3c" stroke-width="2.5"/></svg>
    <svg class="abs" style="left:894px;top:333px" width="38" height="22" viewBox="0 0 38 22" fill="#9bcb3c"><path d="M0 2h7v14H0zM31 2h7v14h-7z"/><path d="M8 4l8-2 7 4 7-2v11l-8 6-14-7z"/></svg>
    <div class="abs feature center" style="left:512px;top:361px"><h3>Experience</h3><p>Over the years the company has gained the knowledge and skills that define the superiority of our product and the rigor of our work ethic.</p></div>
    <div class="abs feature center" style="left:676px;top:361px"><h3>Creativity</h3><p>Our belief is that the key to our clients' success is a combination of innovation, creativity and quality.</p></div>
    <div class="abs feature center" style="left:841px;top:361px"><h3>Professionality</h3><p>We are a family business at the core. Our company is run with the same values as the Ferrante family: respect, determination and commitment.</p></div>
  </section>

  <section class="obm">
    <div class="abs band band-obm" role="img" aria-label="Dimly lit yarn twisting machinery on a factory floor, tinted green"></div>
    <svg class="abs" style="left:554px;top:490px" width="52" height="52" viewBox="0 0 52 52"><circle cx="26" cy="26" r="22" fill="none" stroke="#9bcb3c" stroke-width="2"/></svg>
    <h2 class="abs obm-title"><b>MVYS</b> Open Bridge Method</h2>
    <p class="abs obm-text center">We believe that the key to delivering a yarn that exceeds our client's expectation is to work together with weavers from step one, starting from the desired end product and working backwards. This allows us to develop the product that our weavers need, rather than having weavers adapt to the supplied raw materials.<br>Our Open Bridge Method consists of achieving maximum flexibility both in development and production.</p>
    <a class="abs btn btn-light">FIND OUT MORE <svg width="16" height="6" viewBox="0 0 16 6"><path d="M0 3h15M12 0.5 15 3l-3 2.5" fill="none" stroke="#fff" stroke-width=".8"/></svg></a>
  </section>

  <section class="offers">
    <h2 class="abs section-title center" style="left:441px;top:748px;width:616px">What We Offer</h2>
    <p class="abs section-sub center" style="left:441px;top:791px;width:616px">MVYS combines the experience of a team that has served the weaving industry for over 40 years, fully dedicated to the success of our clients</p>
    <div class="abs offer" style="left:502px;top:818px">
      <div class="offer-img" role="img" aria-label="Business partners shaking hands over a desk with a laptop and documents" style="background:linear-gradient(135deg,#6b4a33 0%,#a58a6e 55%,#d9d2c6 100%)"></div>
      <h3>Network</h3>
      <p>A network of weavers, yarn producers and representatives consolidated over 40 years of successful business operations.</p>
    </div>
    <div class="abs offer" style="left:669px;top:818px">
      <div class="offer-img" role="img" aria-label="Stacked shipping containers at a port under a blue sky" style="background:linear-gradient(180deg,#7fb0dc 0%,#9cc3e4 30%,#7d3b2c 55%,#2c4b6b 80%,#3a5d7c 100%)"></div>
      <h3>Logistics</h3>
      <p>With a distribution grid organized and tuned to perfection, we bring your yarns where you need them, when you need them.</p>
    </div>
    <div class="abs offer" style="left:837px;top:818px">
      <div class="offer-img" role="img" aria-label="Close-up of yarn spinning machines in production" style="background:linear-gradient(135deg,#4b4e4c 0%,#9c9d98 50%,#5d605c 100%)"></div>
      <h3>Production</h3>
      <p>Production line is dynamic and solid, allowing for freedom as well as precision in any project.</p>
    </div>
  </section>

  <section class="team">
    <div class="abs band band-team" role="img" aria-label="Team members standing together, tinted dark green"></div>
    <h2 class="abs section-title center" style="left:441px;top:1063px;width:616px;color:#fff">Our Team</h2>
    <p class="abs section-sub center" style="left:441px;top:1102px;width:616px;color:rgba(255,255,255,.8)">Our team has decades of experience in providing yarn solutions to weavers around the world, assisting them in the creation of outstanding textiles.</p>
    <svg class="abs" style="left:455px;top:1149px" width="16" height="28" viewBox="0 0 16 28"><path d="M14 1 2 14l12 13" fill="none" stroke="#fff" stroke-width="1.5"/></svg>
    <svg class="abs" style="left:1027px;top:1149px" width="16" height="28" viewBox="0 0 16 28"><path d="M2 1l12 13L2 27" fill="none" stroke="#fff" stroke-width="1.5"/></svg>
    <div class="abs portrait" role="img" aria-label="Portrait of founder Aldo Ferrante" style="left:616px;top:1133px;background:linear-gradient(180deg,#e8e8e8,#c9a68f 60%,#2f3c5a)"></div>
    <div class="abs portrait" role="img" aria-label="Portrait of founder Rosanna Belvedere" style="left:769px;top:1133px;background:linear-gradient(180deg,#e6e6e6,#d3a98f 60%,#7c4a6a)"></div>
    <p class="abs member center" style="left:586px;top:1255px">Aldo <b>Ferrante</b> (Founder)</p>
    <p class="abs member center" style="left:742px;top:1255px">Rosanna <b>Belvedere</b> (Founder)</p>
  </section>

  <section class="contact">
    <p class="abs section-sub center" style="left:441px;top:1343px;width:616px;line-height:12px">Our clients can expect open lines of communication, clarity and professionality.<br>Our focus is our client. The success of a client is our success.</p>
    <a class="abs btn btn-green">CONTACT US <svg width="16" height="6" viewBox="0 0 16 6"><path d="M0 3h15M12 0.5 15 3l-3 2.5" fill="none" stroke="#9bcb3c" stroke-width=".8"/></svg></a>
    <svg class="abs" style="left:741px;top:1439px" width="16" height="22" viewBox="0 0 16 22"><path d="M8 21C3 14 1 11 1 8a7 7 0 0 1 14 0c0 3-2 6-7 13z" fill="#9bcb3c"/><circle cx="8" cy="8" r="2.5" fill="#fff"/></svg>
  </section>

  <footer>
    <div class="abs footer"></div>
    <p class="abs copy">© COPYRIGHT 2018 Merovac Novelty Yarn Solutions</p>
    <div class="abs social"><span></span><span></span><span></span><span></span></div>
  </footer>

</div>
</body>
</html>
```